Box Design for Flooring product

***IMPORTANT: PLEASE READ THE DOCUMENT PROVIDED WITH THIS BRIEF CAREFULLY BEFORE ACCEPTING THIS PROJECT***
Need a creative design for the packaging of a flooring product. The packaging is two boxes: one holding 36 planks of flooring, and the other 7 planks of flooring. There are 4 colours for the flooring planks that need a box designed (for both the 36 plank box and 7 plank box). The boxes measures 92 cm x 16cm x 7cm (36 planks) and 92 cm x 16cm x 1.5cm (7 planks).
More details are provided in the requirements document attached with this brief. Also attaching other supporting documents with this brief mentioned in the document.
Need extra days to review
- Montserrat-Regular

```html
<!DOCTYPE html>
<html lang="en">
<head>
<meta charset="utf-8">
<title>Self Adhesive Vinyl Planks – Box Side Panel</title>
<link rel="stylesheet" href="https://fonts.googleapis.com/css2?family=Inter:wght@400;500;700&family=Barlow:wght@400;500;600&display=swap">
<style>
  :root{
    --canvas:#a8a7a5;
    --panel-light:#e7e5e0;
    --panel-white:#ffffff;
    --beige-a:#e2ddd4;
    --beige-b:#cbc4b8;
    --band-dark:#5e5447;
    --band-fade:#8f877b;
    --title-light:#d3cec3;
    --ink:#4d4439;
    --brand:#5e5447;
  }
  html,body{margin:0;padding:0;width:1200px;height:703px;overflow:hidden;background:var(--canvas)}
  .box-panel{position:absolute;left:101px;top:270px;width:988px;height:172px;overflow:hidden}
  .panel-art{position:absolute;left:0;top:0}
  .txt{position:absolute;margin:0;line-height:1;white-space:nowrap}
  .subtitle{font-family:"Inter",sans-serif;font-weight:400;font-size:24px;color:var(--band-dark);left:26px;top:22px}
  .title{font-family:"Inter",sans-serif;font-weight:700;font-size:54px;letter-spacing:-1.5px;color:var(--title-light);left:25px;top:57px}
  .spec-main{font-family:"Barlow",sans-serif;font-weight:400;font-size:13px;color:var(--ink);left:271px;top:14px}
  .spec-size{font-family:"Barlow",sans-serif;font-weight:400;font-size:11.5px;color:var(--ink);left:233px;top:35px}
  .use-ideal{font-family:"Barlow",sans-serif;font-weight:600;font-size:15px;color:var(--ink);right:497px;top:117px;text-align:right;line-height:13.5px}
  .use-domestic{font-family:"Barlow",sans-serif;font-weight:400;font-size:13.2px;color:var(--ink);right:499px;top:151px}
  .feature{position:absolute;top:121px;width:80px;text-align:center;font-family:"Barlow",sans-serif;font-size:9.8px;color:var(--ink)}
  .feature svg{display:block;margin:0 auto 3px}
  .feature--lay{left:26px}
  .feature--water{left:97px}
  .feature--clean{left:171px}
  .brand-name{font-family:"Inter",sans-serif;font-weight:500;font-size:28px;letter-spacing:2px;color:var(--brand);right:26px;top:111px}
</style>
</head>
<body>
<section class="box-panel">
  <svg class="panel-art" width="988" height="172" viewBox="0 0 1647 286">
    <defs>
      <linearGradient id="beige" x1="0" y1="0" x2="1" y2="0">
        <stop offset="0" stop-color="var(--beige-a)"/>
        <stop offset="1" stop-color="var(--beige-b)"/>
      </linearGradient>
      <linearGradient id="band" x1="0" y1="0" x2="1" y2="0">
        <stop offset="0.7" stop-color="var(--band-dark)"/>
        <stop offset="0.95" stop-color="var(--band-fade)"/>
      </linearGradient>
      <linearGradient id="scene" x1="0" y1="0" x2="0" y2="1">
        <stop offset="0" stop-color="#d9d5ce"/>
        <stop offset="0.26" stop-color="#e6e2dc"/>
        <stop offset="0.3" stop-color="#c89552"/>
        <stop offset="1" stop-color="#d7a463"/>
      </linearGradient>
    </defs>
    <rect width="1647" height="286" fill="var(--panel-light)"/>
    <polygon points="467,0 1647,0 1647,286 397,286" fill="url(#beige)"/>
    <polygon points="472,0 967,0 397,286 -100,286" fill="var(--panel-white)"/>
    <rect x="0" y="99" width="832" height="92" fill="url(#band)"/>
    <rect x="832" y="0" width="815" height="286" fill="url(#scene)" role="img" aria-label="Photo of a room with a white door and skirting over light oak vinyl plank flooring"/>
    <polygon points="967,0 832,0 832,68" fill="var(--panel-white)"/>
    <g fill="none" stroke="#fff" stroke-width="3">
      <circle cx="778" cy="145" r="35"/>
      <path d="M756 147 h44 v6 a10 10 0 0 1 -10 10 h-24 a10 10 0 0 1 -10 -10 z" fill="#fff"/>
      <path d="M764 164 l-3 5 M792 164 l3 5"/>
      <path d="M788 147 v-20 h4"/>
    </g>
  </svg>

  <p class="txt subtitle">Self Adhesive</p>
  <h1 class="txt title">Vinyl Planks</h1>
  <p class="txt spec-main">Pack coverage 5m² (36 per planks pack)</p>
  <p class="txt spec-size">Plank size 914mm x 152mm (36” x 6” approx.)</p>
  <p class="txt use-ideal">Ideal for Bathrooms<br>and Kitchens</p>
  <p class="txt use-domestic">Suitable for general domestic use</p>

  <div class="feature feature--lay">
    <svg width="36" height="26" viewBox="0 0 36 26" fill="none" stroke="var(--ink)" stroke-width="1">
      <path d="M1 20 L10 4 H34 L35 20 Z"/>
      <path d="M6 20 L13 4 M12 20 L17 4 M18 20 L21 4 M24 20 L26 4 M30 20 L30 4"/>
      <rect x="15" y="7" width="10" height="7" rx="2" fill="var(--ink)"/>
    </svg>
    Easy to lay
  </div>
  <div class="feature feature--water">
    <svg width="36" height="26" viewBox="0 0 36 26" fill="var(--ink)">
      <path d="M17 5 C20 10 23 13 23 16 a6 6 0 0 1 -12 0 C11 13 14 10 17 5Z"/>
      <path d="M27 2 C28 4 29 5 29 6.5 a2 2 0 0 1 -4 0 C25 5 26 4 27 2Z"/>
      <circle cx="8" cy="16" r="1.2"/><circle cx="6" cy="19" r="1"/>
      <rect x="5" y="23" width="26" height="1.2"/>
    </svg>
    Water resistant
  </div>
  <div class="feature feature--clean">
    <svg width="36" height="26" viewBox="0 0 36 26" fill="var(--ink)">
      <circle cx="21" cy="15" r="9"/>
      <path d="M9 11 l1 2.5 2.5 1 -2.5 1 -1 2.5 -1 -2.5 -2.5 -1 2.5 -1z"/>
      <path d="M15 1 l.7 1.8 1.8 .7 -1.8 .7 -.7 1.8 -.7 -1.8 -1.8 -.7 1.8 -.7z"/>
    </svg>
    Easy to clean
  </div>

  <p class="txt brand-name">NORVALE</p>
</section>
</body>
</html>
```